Business Cards

Need a neat design for a new business card

Industry/Entity Type

Residential Construction

Contact Information for Business Card

Company Name- KORV Construction Inc.
Owner- Daniel Pruitt
Phone number- (555)270-4418
Email- korvcobuilds@mailbox-example.com
Facebook- www.socialpage-example.com/korvcobuilds

Colors
fefdec

```html
<!DOCTYPE html>
<html lang="en">
<head>
<meta charset="utf-8">
<title>KORV Construction Inc. — Business Card</title>
<link href="https://fonts.googleapis.com/css2?family=Montserrat:wght@400;500;700&display=swap" rel="stylesheet">
<style>
  :root {
    --backdrop: #e8e8e6;
    --card: #2b2b2d;
    --card-back: #2f2f31;
    --ink: #fefdec;
    --ink-soft: #d9d8cb;
    --rule: #8a8a86;
    --mark-back: #3d3d40;
  }
  * { margin: 0; padding: 0; box-sizing: border-box; }
  html, body {
    width: 1200px; height: 801px; overflow: hidden;
    background: var(--backdrop);
    font-family: "Montserrat", sans-serif;
  }
  .stage {
    position: relative; width: 1200px; height: 801px;
    display: flex; align-items: center; justify-content: center; gap: 40px;
  }
  .card {
    width: 520px; height: 297px;
    background: var(--card);
    position: relative;
  }
  .card--front { display: flex; align-items: center; }
  .brand {
    width: 238px; text-align: center;
    color: var(--ink); font-weight: 500;
    font-size: 22px; letter-spacing: 1px; line-height: 1.3;
  }
  .divider {
    width: 1px; height: 120px; background: var(--rule);
  }
  .contact { padding-left: 22px; color: var(--ink); }
  .contact__name {
    font-weight: 700; font-size: 19px; letter-spacing: 1px;
    text-transform: uppercase; margin-bottom: 14px;
  }
  .contact__line {
    display: flex; align-items: center; gap: 7px;
    font-size: 12px; font-weight: 400; color: var(--ink-soft);
    margin-bottom: 5px; white-space: nowrap;
  }
  .contact__line svg { width: 11px; height: 11px; flex: none; }
  .icon-square { width: 9px; height: 9px; background: var(--ink-soft); flex: none; margin: 0 1px; }
  .card--back {
    background: var(--card-back);
    display: flex; align-items: center; justify-content: center;
  }
  .brand--back {
    color: var(--mark-back); font-weight: 500; font-size: 30px; letter-spacing: 2px;
  }
</style>
</head>
<body>
<main class="stage">
  <section class="card card--front">
    <div class="brand">KORV<br>Construction Inc.</div>
    <div class="divider"></div>
    <div class="contact">
      <p class="contact__name">Daniel Pruitt</p>
      <p class="contact__line">
        <svg viewBox="0 0 12 12" aria-hidden="true"><circle cx="6" cy="6" r="5.3" fill="none" stroke="#d9d8cb" stroke-width="1"/><path d="M4 3.3 L5 4.6 L4.5 5.3 Q5.4 7 6.8 7.6 L7.5 7 L8.8 8 L8.2 9 Q5 8.7 3.2 4.2 Z" fill="#d9d8cb"/></svg>
        (555)270-4418
      </p>
      <p class="contact__line">
        <svg viewBox="0 0 12 12" aria-hidden="true"><rect x="1" y="3" width="10" height="7" fill="#d9d8cb"/><path d="M1 3 L6 7 L11 3" fill="none" stroke="#2b2b2d" stroke-width="1"/></svg>
        korvcobuilds@mailbox-example.com
      </p>
      <p class="contact__line">
        <span class="icon-square"></span>
        /korvcobuilds
      </p>
    </div>
  </section>
  <section class="card card--back">
    <div class="brand--back">KORV Construction Inc.</div>
  </section>
</main>
</body>
</html>
```